Oil and Gas Exploration and Production company needs a business card design

We need a business card design using our logo and colors in the logo. We want a mainstream design.

```html
<!DOCTYPE html>
<html lang="en">
<head>
<meta charset="utf-8">
<title>Norvale Oil &amp; Gas – Business Card</title>
<link rel="stylesheet" href="https://fonts.googleapis.com/css2?family=Arvo:wght@700&family=Roboto:wght@400&display=swap">
<style>
  :root {
    --stage: #dcd8d2;
    --card-front: #f4f4f3;
    --card-back: #1b1c1d;
    --ink: #111111;
    --gold: #c4952c;
    --body-text: #444444;
    --rule: #222222;
    --white: #ffffff;
  }
  * { margin: 0; padding: 0; box-sizing: border-box; }
  html, body {
    width: 1200px; height: 960px; overflow: hidden;
    background: var(--stage);
  }
  .stage { position: relative; width: 1200px; height: 960px; }

  .card {
    position: absolute; width: 600px; height: 343px;
    box-shadow: 2px 3px 6px rgba(0,0,0,0.35);
  }
  .card--front { left: 314px; top: 113px; background: var(--card-front); overflow: hidden; }
  .card--back { left: 311px; top: 472px; background: var(--card-back); }

  .edge-band { position: absolute; left: 0; top: 0; width: 21px; height: 343px; }

  .brand { position: absolute; left: 54px; top: 40px; display: flex; align-items: center; gap: 14px; }
  .brand__dot { width: 32px; height: 32px; border-radius: 50%; background: var(--ink); }
  .brand__name {
    font-family: "Arvo", Georgia, serif; font-weight: 700; color: var(--ink);
    line-height: 1;
  }
  .brand__name-main { display: block; font-size: 58px; letter-spacing: -1px; }
  .brand__name-sub { display: block; font-size: 22px; letter-spacing: 3px; margin-top: 4px; }

  .person { position: absolute; right: 35px; top: 160px; text-align: right; }
  .person__name {
    font-family: "Arvo", Georgia, serif; font-weight: 700; font-size: 19px;
    color: var(--ink); letter-spacing: 1px;
  }
  .person__title {
    font-family: "Arvo", Georgia, serif; font-weight: 700; font-size: 12.5px;
    color: var(--gold); margin-top: 4px; letter-spacing: 0.3px;
  }

  .divider {
    position: absolute; left: 120px; top: 219px; width: 443px; height: 1.5px;
    background: linear-gradient(to right, rgba(34,34,34,0), var(--rule) 60%);
  }

  .contacts {
    position: absolute; left: 53px; top: 234px; list-style: none;
    font-family: "Roboto", Arial, sans-serif; font-size: 14px; color: var(--body-text);
  }
  .contacts__item { display: flex; align-items: center; height: 19px; }
  .contacts__icon { width: 14px; height: 14px; margin-right: 8px; fill: var(--ink); }

  .address {
    position: absolute; right: 35px; top: 256px; text-align: right;
    font-family: "Roboto", Arial, sans-serif; font-size: 14px; color: var(--body-text);
    line-height: 18.5px; font-style: normal;
  }

  .back-mark {
    position: absolute; left: 449px; top: 212px; width: 56px; height: 56px;
    border: 2px solid var(--white); border-radius: 50%;
  }
  .back-url {
    position: absolute; left: 380px; width: 198px; top: 293px; text-align: center;
    font-family: "Roboto", Arial, sans-serif; font-size: 13px; color: var(--white);
  }
</style>
</head>
<body>
<main class="stage">
  <section class="card card--front" aria-label="Business card front">
    <svg class="edge-band" viewBox="0 0 21 343" aria-hidden="true">
      <polygon points="0,0 21,0 21,115 0,130" fill="var(--gold)"/>
      <polygon points="0,130 21,115 21,343 0,343" fill="var(--ink)"/>
    </svg>

    <div class="brand">
      <span class="brand__dot"></span>
      <span class="brand__name">
        <span class="brand__name-main">Norvale</span>
        <span class="brand__name-sub">OIL &amp; GAS</span>
      </span>
    </div>

    <div class="person">
      <p class="person__name">DANIEL REYES</p>
      <p class="person__title">CEO/FOUNDER</p>
    </div>

    <div class="divider"></div>

    <ul class="contacts">
      <li class="contacts__item">
        <svg class="contacts__icon" viewBox="0 0 16 16" aria-hidden="true"><path d="M3.5 1.5l2.5 0 1 3.5-1.6 1.2c.9 1.9 2.4 3.4 4.3 4.3l1.2-1.6 3.6 1v2.6c0 .8-.7 1.5-1.5 1.5C7.2 14 2 8.8 2 3c0-.8.7-1.5 1.5-1.5z"/></svg>
        612 555 0148
      </li>
      <li class="contacts__item">
        <svg class="contacts__icon" viewBox="0 0 16 16" aria-hidden="true"><path d="M4.5 1h7c.6 0 1 .4 1 1v12c0 .6-.4 1-1 1h-7c-.6 0-1-.4-1-1V2c0-.6.4-1 1-1zm.8 1.8v9h5.4v-9zM8 12.6a.8.8 0 100 1.6.8.8 0 000-1.6z"/></svg>
        612 555 0193
      </li>
      <li class="contacts__item">
        <svg class="contacts__icon" viewBox="0 0 16 16" aria-hidden="true"><path d="M4 1h8v4H4zM1.5 6h13c.3 0 .5.2.5.5V12h-3v3H4v-3H1v-5.5c0-.3.2-.5.5-.5zM5 10v4h6v-4z"/></svg>
        612 555 0176
      </li>
      <li class="contacts__item">
        <svg class="contacts__icon" viewBox="0 0 16 16" aria-hidden="true"><path d="M1.5 3.5h13v.8L8 8.6 1.5 4.3zM1.5 5.6L8 9.9l6.5-4.3v6.9h-13z"/></svg>
        info@norvaleenergy.com
      </li>
    </ul>

    <address class="address">
      2140 Birchwood Drive<br>
      Fairbanks, Alaska 99701<br>
      www.norvaleenergy.com
    </address>
  </section>

  <section class="card card--back" aria-label="Business card back">
    <div class="back-mark"></div>
    <p class="back-url">www.norvaleenergy.com</p>
  </section>
</main>
</body>
</html>
```